Powerpoint template for Tovra - Helping people when they need it the most

Our most urgent need is a powerpoint template with logo, but over time we will also need web design, business card design etc.

We are Tovra Solutions AS, a company delivering innovative services for people when they need it the most.

Our first service, EaseBox (EaseBox by Tovra Solutions), will help people get through all the paperwork and obstacles they meet when they become seriously ill or loose someone close to them. This could typically be automation and digital handling of social security forms, insurance and banking etc.This will free up time for people to focus on recovery or spend time with family.

Our core values are: "Passionate", "Caring" and "Make a difference".
Our vision is (in Norwegian): «EaseBox hjelper deg når du trenger det som mest” which means "EaseBox is there for you when you need it the most".

We need a simple and pure design that:
- Signals to end-users that we are there to help them.
- Signals to investors that Tovra is an innovative company with services based on the latest technology.

The design should include an appropriate logo.
We would like a warm color to be used (we have been using red until now).

Check out our website for more background information: www.tovra-example.no

See also the attached homemade powerpoint presentation that we need to turn into a spectacular pitch! Please do NOT keep much from the original slides.

Target Market(s)

Keep in mind that we are a Scandinavian company.
We want a simple, warm/caring and innovative design that also conveys our tech side.

Industry/Entity Type

Business

Requirements
Must have
• Pictures (of people) - This is all about people
• For our investor pitch we will eventually need slides regarding
• - The problem
• - Our insight / domain knowledge
• - Product/Solution/How it works
• - Vision
• - Market/ Market size / Market potential
• - Business Model
• - Competition / Competetive advantages
• - Plan / Milestones / Timeline
• - The team
• - Strength & weaknesses (including network)
• - Investors / Partners
• - Value proposition
• - Elevator pitch
• - Why Invest (What's in it for the investor)
• - Concerns & Responses
• - Tovra in numbers
• - Financials
• - Q& A
• The slides should reflect that we see ourselves as a tech company (although a caring one) as machine learning, artificial intelligence and robotics.
• In the phase we are in right now we will be interviewing lots of potential users to understand the underlying needs. It would be good to have some pictures to illustrate the interview and user testing situations.
• These are just tips for you to understand what we are occupied with. Please feel free to use you're creativity!
Should not have
• Very bright and exotic colors. We are a Nordic/Scandinavian company

```html
<!DOCTYPE html>
<html lang="en">
<head>
<meta charset="utf-8">
<title>EaseBox by Tovra Solutions – Pitch Template Overview</title>
<link href="https://fonts.googleapis.com/css2?family=Oswald:wght@500;700&family=Open+Sans:wght@400;600;700&display=swap" rel="stylesheet">
<style>
:root{
  --red:#e30613;
  --black:#111111;
  --ink:#333333;
  --sheet:#cfcfcf;
  --white:#ffffff;
  --grey-1:#b3b3b3;
  --grey-2:#9d9d9d;
  --grey-3:#858585;
  --grey-4:#5a5a5a;
  --grey-5:#363636;
}
*{box-sizing:border-box;margin:0;padding:0}
html,body{width:979px;height:1200px;overflow:hidden}
body{background:var(--sheet);position:relative;font-family:"Open Sans",Arial,sans-serif;color:var(--ink)}
.slide{position:absolute;width:420px;height:236px;background:var(--white);box-shadow:0 1px 4px rgba(0,0,0,.25);overflow:hidden}
.slide>svg.deco{position:absolute;left:0;top:0;width:420px;height:236px}
.col-l{left:47px}.col-r{left:512px}
.row-1{top:24px}.row-2{top:316px}.row-3{top:612px}.row-4{top:908px}
.caption{position:absolute;width:420px;text-align:center;font-size:18px;color:#222;letter-spacing:.3px}
.footer{position:absolute;left:0;width:100%;top:222px;text-align:center;font-size:4.5px;letter-spacing:2px;color:#555}
.footer::before,.footer::after{content:"";display:inline-block;width:24px;height:.6px;background:#999;vertical-align:middle;margin:0 6px}
.page-no{position:absolute;right:22px;top:213px;font-size:4.5px;color:#555}
.logo-box{position:absolute;border:1px solid var(--black);font-family:"Oswald",sans-serif;font-weight:700;color:var(--black);text-align:center;letter-spacing:.2px}
.logo-sm{right:14px;top:13px;width:41px;height:14px;font-size:7px;line-height:12px}
.slide-title{position:absolute;font-weight:700;font-size:10px;color:var(--black);padding-bottom:1px;border-bottom:1px solid var(--red)}
.slide-title .hl{color:var(--red)}
.tiny{font-size:4.4px;line-height:6.2px;color:#333}
.tiny-w{font-size:4.4px;line-height:8.8px;color:#fff}
.cover-title{position:absolute;top:10px;width:100%;text-align:center;font-family:"Oswald",sans-serif;font-weight:700;font-size:25px;letter-spacing:-.3px;color:var(--black)}
.cover-title .hl{color:var(--red)}
.cover-logo{left:166px;top:110px;width:88px;height:30px;font-size:17px;line-height:27px;border-width:1.5px}
.problem-text{position:absolute;top:165px;width:86px;text-align:center;font-size:4.2px;line-height:6px}
.insight-list{position:absolute;left:213px;top:79px;width:196px;list-style:none}
.insight-list li{position:relative;padding-left:8px;height:39px;font-size:4.6px;line-height:6.4px}
.insight-list li::before{content:"✓";position:absolute;left:0;top:0;color:var(--red);font-size:5px}
.body-block{position:absolute;text-align:justify}
.market-col{position:absolute;top:36px;width:69px;height:144px;clip-path:polygon(0 0,100% 0,100% 72%,50% 100%,0 72%)}
.market-col p{font-size:4.6px;color:#fff;text-align:center;margin-top:7px;line-height:10.5px}
.market-col p span{display:block;border-bottom:.5px solid rgba(255,255,255,.45);margin:0 5px}
.market-note{position:absolute;left:14px;top:186px;width:392px;text-align:center;font-size:4.4px;line-height:8.5px}
.bm-head{font-size:4.6px;font-weight:700;color:var(--black);margin-bottom:2px}
.team-band{position:absolute;left:0;top:66px;width:100%;height:70px;background:var(--red);color:#fff;text-align:center}
.team-band h3{font-weight:400;font-size:9px;margin-top:3px;margin-bottom:3px}
.team-band p{font-size:4.2px;line-height:5.2px;padding:0 34px;margin-bottom:2px}
.call{position:absolute;top:153px;width:100%;text-align:center;font-size:9.5px;font-weight:600;color:var(--black)}
.call .hl{color:var(--red)}
.contact{position:absolute;top:170px;width:100%;text-align:center;font-size:4.2px;line-height:9.5px}
.back-logo{left:166px;top:18px;width:88px;height:30px;font-size:17px;line-height:27px;border-width:1.5px}
</style>
</head>
<body>

<section class="slide col-l row-1">
  <svg class="deco" viewBox="0 0 420 236">
    <rect x="0" y="51" width="420" height="147" fill="#a9a59e" role="img" aria-label="Photo: elderly man walking with a cane on a snowy path"/>
    <polygon points="210,52 283,125 210,198 137,125" fill="#fff"/>
    <polygon points="0,206 0,236 30,236" fill="var(--red)"/>
    <polygon points="420,206 420,236 390,236" fill="var(--red)"/>
  </svg>
  <h1 class="cover-title"><span class="hl">EASEBOX</span> BY TOVRA <span class="hl">SOLUTIONS</span></h1>
  <div class="logo-box cover-logo">LOGO HERE</div>
  <div class="footer">www.tovra-example.no</div>
</section>
<div class="caption col-l" style="top:276px">COVER PAGE</div>

<section class="slide col-r row-1">
  <svg class="deco" viewBox="0 0 420 236">
    <g id="prob">
      <polygon points="80,45 126,91 80,137 34,91" fill="var(--black)"/>
      <polyline points="36,82 31,91 36,100" fill="none" stroke="var(--red)" stroke-width="1.2"/>
      <polyline points="124,82 129,91 124,100" fill="none" stroke="var(--red)" stroke-width="1.2"/>
      <line x1="80" y1="137" x2="80" y2="157" stroke="var(--red)" stroke-width=".8" stroke-dasharray="1.5 1.5"/>
      <circle cx="80" cy="131" r="2" fill="var(--red)"/>
      <circle cx="80" cy="157" r="1.8" fill="var(--red)"/>
      <circle cx="80" cy="91" r="16" fill="var(--red)"/>
    </g>
    <use href="#prob" x="131"/>
    <use href="#prob" x="263"/>
    <text x="80" y="98" text-anchor="middle" font-family="Oswald,sans-serif" font-weight="700" font-size="20" fill="#111">?</text>
    <circle cx="211" cy="91" r="6" fill="none" stroke="#111" stroke-width="3" stroke-dasharray="2.4 1.6"/>
    <circle cx="211" cy="91" r="2" fill="#111"/>
    <rect x="335" y="89" width="16" height="4" fill="#111"/>
    <rect x="341" y="83" width="4" height="16" fill="#111"/>
    <polygon points="0,206 0,236 30,236" fill="var(--red)"/>
    <polygon points="420,206 420,236 390,236" fill="var(--red)"/>
  </svg>
  <h2 class="slide-title" style="left:12px;top:12px"><span class="hl">THE</span> PROBLEM</h2>
  <div class="logo-box logo-sm">LOGO HERE</div>
  <p class="problem-text" style="left:37px">Short sample text for the problem area of the slide. Sample text has been the industry's standard.</p>
  <p class="problem-text" style="left:168px">Short sample text for the problem area of the slide. Sample text has been the industry's standard.</p>
  <p class="problem-text" style="left:300px">Short sample text for the problem area of the slide. Sample text has been the industry's standard.</p>
  <div class="page-no">01</div>
  <div class="footer">www.tovra-example.no</div>
</section>
<div class="caption col-r" style="top:276px">PAGE - 01</div>

<section class="slide col-l row-2">
  <svg class="deco" viewBox="0 0 420 236">
    <polygon points="0,0 72,0 150,104 60,236 0,236" fill="var(--red)"/>
    <polygon points="60,236 150,104 175,118 90,236" fill="#fff"/>
    <polyline points="92,0 205,118 92,236" fill="none" stroke="var(--red)" stroke-width="1"/>
    <rect x="113" y="73" width="70" height="70" rx="8" transform="rotate(45 148 108)" fill="var(--black)"/>
    <rect x="68" y="68" width="76" height="76" rx="8" transform="rotate(45 106 106)" fill="#c7b88a" role="img" aria-label="Photo: carer walking with a person in a wheelchair at sunset"/>
    <polygon points="420,206 420,236 390,236" fill="var(--red)"/>
  </svg>
  <div class="logo-box logo-sm">LOGO HERE</div>
  <h2 class="slide-title" style="left:213px;top:48px"><span class="hl">OUR INSIGHT</span> / DOMAIN KNOWLEDGE</h2>
  <ul class="insight-list">
    <li>Sample text is simply placeholder copy of the printing and typesetting trade. Sample text has been the trade's standard filler.</li>
    <li>Sample text is simply placeholder copy of the printing and typesetting trade. Sample text has been the trade's standard filler.</li>
    <li>Sample text is simply placeholder copy of the printing and typesetting trade. Sample text has been the trade's standard filler.</li>
  </ul>
  <div class="page-no">02</div>
  <div class="footer">www.tovra-example.no</div>
</section>
<div class="caption col-l" style="top:568px">PAGE - 02</div>

<section class="slide col-r row-2">
  <svg class="deco" viewBox="0 0 420 236">
    <rect x="198" y="28" width="180" height="180" rx="10" transform="rotate(45 288 118)" fill="none" stroke="var(--black)" stroke-width="1.6"/>
    <rect x="222" y="48" width="140" height="140" rx="12" transform="rotate(45 292 118)" fill="var(--red)"/>
    <rect x="230" y="40" width="124" height="124" rx="12" transform="rotate(45 292 102)" fill="#6c8f3e" role="img" aria-label="Photo: older man resting on the grass beside his bicycle in a park"/>
    <polygon points="0,206 0,236 30,236" fill="var(--red)"/>
    <polygon points="420,206 420,236 390,236" fill="var(--red)"/>
  </svg>
  <h2 class="slide-title" style="left:12px;top:12px"><span class="hl">PRODUCT/SOLUTION/</span>HOW IT WORKS</h2>
  <div class="logo-box logo-sm">LOGO HERE</div>
  <p class="body-block tiny" style="left:12px;top:54px;width:150px">Sample text is simply placeholder copy of the printing and typesetting trade. Sample text has been the trade's standard filler ever since the early days, when an unknown printer took a tray of type and mixed it to make a type sample book. It has survived not only many decades, but also the leap into digital typesetting, remaining largely unchanged. It became popular with the release of transfer sheets containing sample passages, and more recently with desktop layout software including versions of sample text.</p>
  <p class="body-block tiny" style="left:12px;top:146px;width:150px">Sample text is simply placeholder copy of the printing and typesetting trade. Sample text has been the trade's standard filler ever since the early days, when an unknown printer took a tray of type and mixed it to make a type sample book.</p>
  <div class="page-no">03</div>
  <div class="footer">www.tovra-example.no</div>
</section>
<div class="caption col-r" style="top:568px">PAGE - 03</div>

<section class="slide col-l row-3">
  <svg class="deco" viewBox="0 0 420 236">
    <polygon points="0,55 254,55 190,136 254,184 0,184" fill="var(--black)"/>
    <rect x="276" y="51" width="130" height="130" rx="10" transform="rotate(45 341 116)" fill="none" stroke="var(--black)" stroke-width="1.6"/>
    <rect x="283" y="68" width="110" height="110" rx="10" transform="rotate(45 338 123)" fill="var(--red)"/>
    <rect x="288" y="52" width="102" height="102" rx="10" transform="rotate(45 339 103)" fill="#a7a5a2" role="img" aria-label="Photo: smiling elderly woman with white hair"/>
    <polygon points="0,206 0,236 30,236" fill="var(--red)"/>
  </svg>
  <h2 class="slide-title" style="left:12px;top:12px;color:var(--red)">VISION</h2>
  <p class="body-block tiny-w" style="left:12px;top:64px;width:188px">Sample text is simply placeholder copy of the printing and typesetting trade. Sample text has been the trade's standard filler ever since the early days, when an unknown printer took a tray of type and mixed it to make a type sample book. It has survived not only many decades, but also the leap into digital typesetting, remaining largely unchanged. It became popular with transfer sheets and desktop layout software.</p>
  <p class="body-block tiny-w" style="left:12px;top:140px;width:188px">Sample text is simply placeholder copy of the printing and typesetting trade. Sample text has been the trade's standard filler ever since the early days, when an unknown printer mixed type to make a sample book.</p>
  <div class="page-no">04</div>
  <div class="footer">www.tovra-example.no</div>
</section>
<div class="caption col-l" style="top:864px">PAGE - 04</div>

<section class="slide col-r row-3">
  <h2 class="slide-title" style="left:12px;top:12px"><span class="hl">MARKET/ MARKET SIZE</span> / MARKET POTENTIAL</h2>
  <div class="market-col" style="left:13px;background:var(--grey-1)"><p><span>Sample text is simply</span><span>Sample text is simply</span><span>Sample text is simply</span><span>Sample text is simply</span></p></div>
  <div class="market-col" style="left:94px;background:var(--grey-2)"><p><span>Sample text is simply</span><span>Sample text is simply</span><span>Sample text is simply</span><span>Sample text is simply</span></p></div>
  <div class="market-col" style="left:175px;background:var(--grey-3)"><p><span>Sample text is simply</span><span>Sample text is simply</span><span>Sample text is simply</span><span>Sample text is simply</span></p></div>
  <div class="market-col" style="left:256px;background:var(--grey-4)"><p><span>Sample text is simply</span><span>Sample text is simply</span><span>Sample text is simply</span><span>Sample text is simply</span></p></div>
  <div class="market-col" style="left:337px;background:var(--grey-5)"><p><span>Sample text is simply</span><span>Sample text is simply</span><span>Sample text is simply</span><span>Sample text is simply</span></p></div>
  <svg class="deco" viewBox="0 0 420 236">
    <g fill="#fff" stroke="none">
      <polygon points="47.5,125 70,147 47.5,170 25,147"/>
      <polygon points="128.5,125 151,147 128.5,170 106,147"/>
      <polygon points="209.5,125 232,147 209.5,170 187,147"/>
      <polygon points="290.5,125 313,147 290.5,170 268,147"/>
      <polygon points="371.5,125 394,147 371.5,170 349,147"/>
    </g>
    <g fill="none" stroke-width="1.2">
      <polygon points="47.5,128 67,147 47.5,167 28,147" stroke="var(--grey-1)"/>
      <polygon points="128.5,128 148,147 128.5,167 109,147" stroke="var(--grey-2)"/>
      <polygon points="209.5,128 229,147 209.5,167 190,147" stroke="var(--grey-3)"/>
      <polygon points="290.5,128 310,147 290.5,167 271,147" stroke="var(--grey-4)"/>
      <polygon points="371.5,128 391,147 371.5,167 352,147" stroke="var(--grey-5)"/>
    </g>
    <circle cx="47.5" cy="147" r="5" fill="var(--grey-1)"/>
    <circle cx="128.5" cy="147" r="5" fill="var(--grey-2)"/>
    <circle cx="209.5" cy="147" r="5" fill="var(--grey-3)"/>
    <circle cx="290.5" cy="147" r="5" fill="var(--grey-4)"/>
    <circle cx="371.5" cy="147" r="5" fill="var(--grey-5)"/>
    <polygon points="0,206 0,236 30,236" fill="var(--red)"/>
    <polygon points="420,206 420,236 390,236" fill="var(--red)"/>
  </svg>
  <p class="market-note">Sample text is simply placeholder copy of the printing and typesetting trade. Sample text has been the trade's standard filler ever since the early days, when an unknown printer took a tray of type and mixed it to make a type sample book. It has survived many decades.</p>
  <div class="page-no">05</div>
  <div class="footer">www.tovra-example.no</div>
</section>
<div class="caption col-r" style="top:864px">PAGE - 05</div>

<section class="slide col-l row-4">
  <svg class="deco" viewBox="0 0 420 236">
    <g id="bm">
      <polygon points="53,35 90,72 53,109 16,72" fill="var(--black)"/>
      <polyline points="19,64 14,72 19,80" fill="none" stroke="var(--red)" stroke-width="1.2"/>
      <polyline points="87,64 92,72 87,80" fill="none" stroke="var(--red)" stroke-width="1.2"/>
      <circle cx="53" cy="66" r="6" fill="#fff"/>
      <rect x="44" y="74" width="18" height="10" rx="4" fill="#fff"/>
    </g>
    <use href="#bm" x="228"/>
    <line x1="210" y1="64" x2="210" y2="180" stroke="#999" stroke-width=".6" stroke-dasharray="1.5 1.5"/>
    <polygon points="0,206 0,236 30,236" fill="var(--red)"/>
    <polygon points="420,206 420,236 390,236" fill="var(--red)"/>
  </svg>
  <h2 class="slide-title" style="left:12px;top:12px"><span class="hl">BUSINESS</span> MODEL</h2>
  <div class="logo-box logo-sm">LOGO HERE</div>
  <div class="body-block tiny" style="left:102px;top:56px;width:80px"><div class="bm-head">SAMPLE TITLE</div>Sample text is simply placeholder copy of the printing and typesetting trade. Sample text has been the trade's standard.</div>
  <div class="body-block tiny" style="left:330px;top:56px;width:80px"><div class="bm-head">SAMPLE TITLE</div>Sample text is simply placeholder copy of the printing and typesetting trade. Sample text has been the trade's standard.</div>
  <div class="body-block tiny" style="left:13px;top:139px;width:172px"><div class="bm-head">SAMPLE TEXT IS SIMPLY PLACEHOLDER COPY OF THE PRINTING</div>Sample text is simply placeholder copy of the printing and typesetting trade. Sample text has been the trade's standard filler ever since the early days, when an unknown printer took a tray of type and mixed it to make a type sample book. It has survived many decades.</div>
  <div class="body-block tiny" style="left:243px;top:139px;width:165px"><div class="bm-head">SAMPLE TEXT IS SIMPLY PLACEHOLDER COPY OF THE PRINTING</div>Sample text is simply placeholder copy of the printing and typesetting trade. Sample text has been the trade's standard filler ever since the early days, when an unknown printer took a tray of type and mixed it to make a type sample book. It has survived many decades.</div>
  <div class="page-no">06</div>
  <div class="footer">www.tovra-example.no</div>
</section>
<div class="caption col-l" style="top:1160px">PAGE - 06</div>

<section class="slide col-r row-4">
  <div class="logo-box back-logo">LOGO HERE</div>
  <div class="team-band">
    <h3>TEAM TOVRA</h3>
    <p>We are two people who genuinely care about the opportunities technology gives for simplifying people's everyday lives. By finding the meeting point of physical and digital that gives good user experiences, we can add real and meaningful value to our customers and users. Our background spans business development, project management, sales management and technology.</p>
    <p>We are in Eastport and Northvale.</p>
    <p>Team Tovra takes part in the incubator program, Social Start Challenge, at the Nordic Work Hub.<br>In addition, Team Tovra also takes part in the startup investment program, Seed Challenge, for Startup Seed Challenge.</p>
  </div>
  <div class="call"><span class="hl">CALL US TODAY</span>&nbsp; (+47) 40000000</div>
  <div class="contact">
    <svg width="4" height="5" viewBox="0 0 4 5" style="vertical-align:middle"><path d="M2 0a2 2 0 0 1 2 2c0 1.3-2 3-2 3S0 3.3 0 2a2 2 0 0 1 2-2z" fill="#111"/></svg>
    Tovra Solutions AS Company No. 900000000<br>
    <svg width="5" height="4" viewBox="0 0 5 4" style="vertical-align:middle"><rect width="5" height="4" fill="#111"/><polyline points="0,0 2.5,2 5,0" fill="none" stroke="#fff" stroke-width=".5"/></svg>
    hello@tovra-example.no
  </div>
  <svg class="deco" viewBox="0 0 420 236">
    <polygon points="0,206 0,236 30,236" fill="var(--red)"/>
    <polygon points="420,206 420,236 390,236" fill="var(--red)"/>
  </svg>
  <div class="footer">www.tovra-example.no</div>
</section>
<div class="caption col-r" style="top:1158px">BACK PAGE</div>

</body>
</html>
```